Visitenkarten-Design für Kfz-Werkstatt von Frauen für Frauen
Zielgruppe
Kfz-Werkstatt von Frauen für Frauen
Aufgabenstellung
Die Farben des Logos sollen sich in der Visitenkarte wieder spiegeln. Darf sehr feminin gehalten werden!
Infos auf der Visistenkarte:

```html
<!DOCTYPE html>
<html lang="de">
<head>
<meta charset="utf-8">
<title>Visitenkarte Veltmoor GmbH</title>
<link href="https://fonts.googleapis.com/css2?family=Montserrat:wght@400;500&display=swap" rel="stylesheet">
<style>
  :root {
    --backdrop: #e8d9d9;
    --card: #f7f6f5;
    --magenta: #d41c5c;
    --magenta-dark: #b8164f;
    --ink: #4a4a4a;
    --shadow: rgba(90, 60, 60, 0.22);
  }
  * { margin: 0; padding: 0; box-sizing: border-box; }
  html, body {
    width: 1200px; height: 864px; overflow: hidden;
    background: var(--backdrop);
    font-family: "Montserrat", sans-serif;
  }
  .stage { position: relative; width: 1200px; height: 864px; }
  .card {
    position: absolute;
    width: 540px; height: 310px;
    background: var(--card);
    box-shadow: 0 14px 30px var(--shadow);
  }
  .card--front { left: 150px; top: 120px; }
  .card--back { left: 510px; top: 434px; }

  .contact-list {
    position: absolute; left: 50px; top: 64px;
    list-style: none;
    display: flex; flex-direction: column; gap: 16px;
  }
  .contact-item { display: flex; align-items: center; gap: 22px; }
  .contact-icon {
    width: 32px; height: 32px; border-radius: 50%;
    background: linear-gradient(135deg, var(--magenta), var(--magenta-dark));
    display: flex; align-items: center; justify-content: center;
    flex-shrink: 0;
  }
  .contact-icon svg { width: 16px; height: 16px; }
  .contact-text { color: var(--ink); font-size: 12.5px; line-height: 1.35; letter-spacing: 0.02em; }

  .company-name {
    position: absolute; right: 40px; top: 110px;
    color: var(--magenta); font-size: 19px; font-weight: 500;
  }

  .brand {
    position: absolute; left: 0; right: 0; top: 0; bottom: 0;
    display: flex; align-items: center; justify-content: center; gap: 14px;
  }
  .brand-dot { width: 18px; height: 18px; border-radius: 50%; background: var(--magenta); }
  .brand-name { color: var(--magenta); font-size: 34px; font-weight: 500; letter-spacing: 0.08em; }
</style>
</head>
<body>
<main class="stage">
  <section class="card card--front">
    <ul class="contact-list">
      <li class="contact-item">
        <span class="contact-icon">
          <svg viewBox="0 0 16 16"><path d="M8 1.5a4.5 4.5 0 0 0-4.5 4.5c0 3.3 4.5 8.5 4.5 8.5s4.5-5.2 4.5-8.5A4.5 4.5 0 0 0 8 1.5zm0 6.2a1.7 1.7 0 1 1 0-3.4 1.7 1.7 0 0 1 0 3.4z" fill="#fff"/></svg>
        </span>
        <span class="contact-text">Lindenhofer Str. 12<br>80000 Musterstadt</span>
      </li>
      <li class="contact-item">
        <span class="contact-icon">
          <svg viewBox="0 0 16 16"><rect x="2" y="4" width="12" height="8" fill="none" stroke="#fff" stroke-width="1.3"/><path d="M2 4l6 5 6-5M2 12l4.5-4M14 12l-4.5-4" fill="none" stroke="#fff" stroke-width="1.1"/></svg>
        </span>
        <span class="contact-text">hallo@werkstatt-rosalie.de</span>
      </li>
      <li class="contact-item">
        <span class="contact-icon">
          <svg viewBox="0 0 16 16"><path d="M4.2 2.5l2 2.6-1.2 1.3a8 8 0 0 0 4.6 4.6l1.3-1.2 2.6 2-1.3 1.7C8 13.3 2.7 8 2.5 3.8z" fill="#fff"/></svg>
        </span>
        <span class="contact-text">0150 - 12 34 56 7</span>
      </li>
      <li class="contact-item">
        <span class="contact-icon">
          <svg viewBox="0 0 16 16" fill="none" stroke="#fff" stroke-width="1.2"><circle cx="8" cy="8" r="5.8"/><ellipse cx="8" cy="8" rx="2.6" ry="5.8"/><path d="M2.2 8h11.6M3 5h10M3 11h10"/></svg>
        </span>
        <span class="contact-text">www.werkstatt-rosalie.de</span>
      </li>
    </ul>
    <p class="company-name">Veltmoor GmbH</p>
  </section>

  <section class="card card--back">
    <div class="brand">
      <span class="brand-dot"></span>
      <span class="brand-name">VELTMOOR</span>
    </div>
  </section>
</main>
</body>
</html>
```